E-Liquid Label Design for Lantern Mist

We need a new design for the labels we use on our product, which are bottles of e-liquid for use in e-cigarettes. We have attached our original label (which we are using now) so you can see what we are using. We would like a new design that is classier, like the label on a high end bottle of rum or whisky, but with a little bit of a modern flair. I have also attached examples of our competitors bottles. We do not necessarily want our new design to be too similar to these, in an effort to avoid copying them, but we want the new design to be up to par with them in terms of quality and appeal.
The label must contain the following information:
- Bottle Size : 30ml
- Type of blend (Either 50PG/50VG or 70PG/30VG). The new design can have this set statically. We only included both options on the original label because we manually mark this with a marker depending on what blend it is. We no longer want to do this. We just want the one blend, whatever it is to be on the label.
- The line "Orchard Drip" (as this is the name of the line)
- The line "Premium E-Liquid" in smaller caps right under "Orchard Drip"
- The Flavor Name
- The Nicotine strength. You can use the example strength "FULL | 2.4 Nicotine"
- The Ingredients and Warning. See original label for text (Including "Shake Well")
- A small white box where a UPC barcode can be placed
Use the color theme on the original label, but you can mix it up and use more of one color than another. Be as creative as possible. Classy & Tropical would be what someone would think of when looking at this new design.
Our High Res Logo is also attached.New Label stock that will be used with be white high gloss 1X2.5
The final design must be in .svg format so we can change the variables, like bottles size, flavor, etc when printing.

```html
<!DOCTYPE html>
<html lang="en">
<head>
<meta charset="utf-8">
<title>Lantern Mist – Orchard Drip Label Options</title>
<link rel="stylesheet" href="https://fonts.googleapis.com/css2?family=Arimo:wght@400;700&family=Lobster&display=swap">
<style>
  :root {
    --page: #ffffff;
    --ink: #111111;
    --leaf-pale: #e6efbf;
    --leaf-light: #cfe29a;
    --leaf-mid: #8dbb4c;
    --leaf-deep: #2f7a3a;
    --leaf-dark: #1f5e2c;
    --brand-green: #3f8a2e;
    --lime-text: #b5d334;
    --panel-edge: #b9d27a;
    --white: #ffffff;
    --shadow: rgba(0,0,0,.55);
  }
  html, body { margin: 0; padding: 0; overflow: hidden; }
  body { width: 1200px; height: 1157px; background: var(--page); position: relative; font-family: "Arimo", Arial, sans-serif; color: var(--ink); }
  .option-letter { position: absolute; left: 96px; font-size: 118px; font-weight: 400; line-height: 1; }
  .option-letter--a { top: 262px; }
  .option-letter--b { top: 752px; }

  .label { position: absolute; left: 270px; width: 832px; height: 421px; border-radius: 12px; overflow: hidden; box-shadow: 0 0 0 1px #c9d59c; }
  .label--a { top: 118px; background: linear-gradient(180deg, var(--leaf-pale), var(--leaf-light)); }
  .label--b { top: 612px; background: linear-gradient(180deg, var(--leaf-pale) 0%, #d7e8a3 35%, var(--leaf-light) 100%); }
  .label__art { position: absolute; inset: 0; }

  .ingredients, .warning { position: absolute; left: 24px; width: 200px; font-size: 12.5px; line-height: 1.3; }
  .ingredients { top: 100px; }
  .ingredients h3, .warning h3 { margin: 0; font-size: 12.5px; font-weight: 700; }
  .warning { top: 258px; }
  .label--a .warning { color: var(--white); }
  .warning ul { margin: 0; padding: 0 0 0 14px; list-style: none; }
  .warning li::before { content: "- "; margin-left: -9px; }

  .brand { position: absolute; left: 250px; top: 46px; width: 290px; display: flex; align-items: center; justify-content: center; gap: 10px; }
  .brand__dot { width: 26px; height: 26px; border-radius: 50%; background: var(--brand-green); }
  .brand__name { font-size: 36px; font-weight: 700; color: var(--brand-green); letter-spacing: .5px; }

  .line-name { position: absolute; left: 210px; width: 340px; text-align: center; font-weight: 700; margin: 0; }
  .line-name__title { font-size: 36px; line-height: 1; }
  .line-name__sub { font-size: 23px; line-height: 1.1; margin-top: 4px; }
  .label--a .line-name { top: 162px; color: var(--ink); }
  .label--b .line-name { top: 176px; }
  .label--b .line-name__title { color: var(--lime-text); -webkit-text-stroke: 1px #4c6a12; }
  .label--b .line-name__sub { color: var(--brand-green); -webkit-text-stroke: .4px #27501b; }

  .flavor { position: absolute; left: 210px; width: 340px; text-align: center; font-family: "Lobster", cursive; font-size: 58px; line-height: 1; }
  .label--a .flavor { top: 282px; color: var(--white); text-shadow: 2px 3px 2px var(--shadow); }
  .label--b .flavor { top: 285px; color: #8a8a8a; -webkit-text-stroke: 1.5px #3a3a3a; text-shadow: 2px 2px 0 var(--white); }

  .strength { position: absolute; left: 210px; width: 340px; top: 373px; text-align: center; font-size: 18px; }
  .label--a .strength { color: var(--white); }
  .label--b .strength { color: var(--ink); }

  .vertical { position: absolute; writing-mode: vertical-rl; transform: rotate(180deg); white-space: nowrap; text-align: center; }
  .blend { font-size: 23px; }
  .label--a .blend { left: 710px; top: 18px; height: 210px; }
  .label--b .blend { left: 672px; top: 10px; height: 160px; }
  .upc-note { font-size: 12.5px; }
  .label--a .upc-note { left: 680px; top: 250px; height: 100px; }

  .upc-box { position: absolute; left: 637px; top: 171px; width: 98px; height: 234px; background: var(--white); }
  .upc-box .vertical { position: static; height: 234px; width: 98px; font-size: 20px; line-height: 98px; }
</style>
</head>
<body>
  <div class="option-letter option-letter--a">A</div>
  <div class="option-letter option-letter--b">B</div>

  <section class="label label--a" aria-label="Label option A">
    <svg class="label__art" width="832" height="421" viewBox="0 0 832 421" aria-hidden="true">
      <defs>
        <linearGradient id="bandA" x1="0" y1="0" x2="1" y2="0">
          <stop offset="0" stop-color="#2a7436"/>
          <stop offset=".55" stop-color="#2f7d3a"/>
          <stop offset="1" stop-color="#4f9a45"/>
        </linearGradient>
      </defs>
      <rect x="0" y="245" width="832" height="176" fill="url(#bandA)"/>
      <path d="M0 245 C180 240 360 236 520 250 C600 258 640 300 660 421 L0 421 Z" fill="#2a6f34" opacity=".6"/>
      <path d="M470 245 C560 250 620 290 700 421 L832 421 L832 245 Z" fill="#5ea24c" opacity=".45"/>
      <rect x="661" y="0" width="99" height="421" fill="#eef5d2" opacity=".55"/>
      <rect x="760" y="0" width="72" height="421" fill="#d9e9a8" opacity=".6"/>
      <line x1="661" y1="0" x2="661" y2="421" stroke="var(--panel-edge)" stroke-width="1"/>
      <line x1="760" y1="0" x2="760" y2="421" stroke="var(--panel-edge)" stroke-width="1"/>
    </svg>

    <div class="ingredients"><h3>Ingredients</h3>USP Grade Vegetable Glycerin, USP Grade Propylene Glycol Flavors, Artificial Flavors.</div>
    <div class="brand"><span class="brand__dot"></span><span class="brand__name">Lantern Mist</span></div>
    <h2 class="line-name"><div class="line-name__title">Orchard Drip</div><div class="line-name__sub">Premium E-Liquid</div></h2>
    <div class="warning"><h3>WARNING</h3><ul><li>Keep out of reach of children.</li><li>Must be 18 or older.</li><li>Do not drink.</li><li>Shake Well</li></ul></div>
    <div class="flavor">Chocolate</div>
    <div class="strength">FULL | 2.4 Nicotine | 30ml</div>
    <div class="vertical blend">50PG/50VG</div>
    <div class="vertical upc-note">UPC<br>barcode</div>
  </section>

  <section class="label label--b" aria-label="Label option B">
    <svg class="label__art" width="832" height="421" viewBox="0 0 832 421" aria-hidden="true">
      <defs>
        <linearGradient id="glassB" x1="0" y1="0" x2="1" y2="0">
          <stop offset="0" stop-color="#ffffff" stop-opacity="0"/>
          <stop offset=".3" stop-color="#ffffff" stop-opacity=".75"/>
          <stop offset=".7" stop-color="#ffffff" stop-opacity=".75"/>
          <stop offset="1" stop-color="#ffffff" stop-opacity="0"/>
        </linearGradient>
        <linearGradient id="lowerB" x1="0" y1="0" x2="0" y2="1">
          <stop offset="0" stop-color="#6fae3a"/>
          <stop offset=".5" stop-color="#8dc04b"/>
          <stop offset="1" stop-color="#7ab43f"/>
        </linearGradient>
      </defs>
      <rect x="0" y="147" width="832" height="115" fill="#9cc75a" opacity=".55"/>
      <rect x="80" y="147" width="600" height="115" fill="url(#glassB)"/>
      <rect x="0" y="262" width="832" height="159" fill="url(#lowerB)"/>
      <ellipse cx="380" cy="340" rx="260" ry="60" fill="#c6e08a" opacity=".45"/>
      <rect x="760" y="0" width="72" height="421" fill="#eef5d2" opacity=".5"/>
      <line x1="760" y1="0" x2="760" y2="421" stroke="var(--panel-edge)" stroke-width="1"/>
    </svg>

    <div class="ingredients"><h3>Ingredients</h3>USP Grade Vegetable Glycerin, USP Grade Propylene Glycol Flavors, Artificial Flavors.</div>
    <div class="brand"><span class="brand__dot"></span><span class="brand__name">Lantern Mist</span></div>
    <h2 class="line-name"><div class="line-name__title">Orchard Drip</div><div class="line-name__sub">Premium E-Liquid</div></h2>
    <div class="warning"><h3>WARNING</h3><ul><li>Keep out of reach of children.</li><li>Must be 18 or older.</li><li>Do not drink.</li><li>Shake Well</li></ul></div>
    <div class="flavor">Chocolate</div>
    <div class="strength">FULL | 2.4 Nicotine | 30ml</div>
    <div class="vertical blend">50PG/50VG</div>
    <div class="upc-box"><div class="vertical">UPC barcode</div></div>
  </section>
</body>
</html>
```